Looking for a modern elegant home improvment website

Looking for a new Design on current website . Please us www.larkfieldbuilders.example PIctures of recent work and stock photos that were attached , Free estimates , Explaining what we do , Similiar to www. larkfieldbuilders.example which is our current webpage . Colors can be different . I have attached our buisness card as well as our postcard we send out to homes . I would like a modern web page that our costumers can feel is professional so they can have a feeling of trust when they hire us . Our address should be on there . Licenesed & Insured should be somewhere on the page . Our Company Logo should be there as well . It would be nice to have a very modern website with great pictures of home interiors and exteriors . a page describing what we do is very important . facebook link to our page is a must as well as a instagram .
Updates

Reason: Looking for a elegant modern 5 page website with proper spelling and professional looking . I extended the deadline and upgraded .

Reason: Looking for more design options .

Target Market(s)

Home owners , Commerical buisness,

Industry/Entity Type

Home Improvement

Number of Pages Required

5+ page

Font styles to use
Serif

Requirements
Must have
• PIctures of recent work and stock photos that were attached , Free estimates , Explaining what we do , Similiar to www. larkfieldbuilders.example which is our current webpage . Colors can be different . I have attached our buisness card as well as our postcard we send out to homes . I would like a modern web page that our costumers can feel is professional so they can have a feeling of trust when they hire us . Our address should be on there . Licenesed & Insured should be somewhere on the page . Our Company Logo should be there as well .
Nice to have
• It would be nice to have a very modern website with great pictures of home interiors and exteriors . a page describing what we do is very important . facebook link to our page is a must as well as a instagram .

```html
<!DOCTYPE html>
<html lang="en">
<head>
<meta charset="utf-8">
<title>Larkfield Builders LLC</title>
<link href="https://fonts.googleapis.com/css2?family=Cinzel:wght@400;700&family=Open+Sans:wght@400;600;700&display=swap" rel="stylesheet">
<style>
:root{
  --green:#0b4d2c;
  --green-2:#13633a;
  --navy:#3d4f85;
  --navy-dark:#2f3f6e;
  --grey-bg:#ececec;
  --ink:#2b2b2b;
  --muted:#555;
  --footer:#1f1f1f;
  --white:#fff;
}
*{box-sizing:border-box;margin:0;padding:0}
html,body{width:1200px;height:3719px;overflow:hidden;background:#fff}
body{position:relative;font-family:"Open Sans",Arial,sans-serif;color:var(--ink)}
.abs{position:absolute}

/* header */
.topbar{top:6px;right:78px;display:flex;align-items:center;gap:10px;color:var(--white);background:var(--navy);height:30px;padding:0 16px;border-radius:0 0 0 14px;font-size:20px}
.topbar .dot{width:18px;height:18px;border-radius:50%;background:#fff}
.topbar .phone{display:flex;align-items:center;gap:8px}
.topbar .phone i{width:20px;height:20px;border-radius:50%;background:#2e9e4a;display:inline-block}
.brand{left:84px;top:40px;font-family:"Cinzel",Georgia,serif;font-size:24px;color:var(--green);font-weight:700;letter-spacing:.5px}
.brand small{display:block;font-size:12px;letter-spacing:4px;text-align:center;font-weight:400;color:var(--green)}
.nav{top:64px;left:552px;display:flex;gap:34px;font-family:"Cinzel",Georgia,serif;font-size:22px;color:#111}
.nav .home{width:22px;height:22px}

/* hero */
.hero-photo{left:0;top:118px;width:640px;height:520px;background:linear-gradient(135deg,#5a3416,#a9692e 45%,#d4a86a 70%,#6d4220)}
.hero-curve{left:0;top:470px;width:1200px;height:190px}
.hero-accent{left:560px;top:118px;width:90px;height:340px}
.hero-brand{left:650px;top:200px;width:470px;text-align:center;font-family:"Cinzel",Georgia,serif;color:var(--green)}
.hero-brand .name{font-size:30px;font-weight:700}
.hero-brand .tag{font-size:16px;letter-spacing:6px;margin-top:4px}
.estimate{left:690px;top:292px;width:425px;height:82px;background:var(--navy);clip-path:polygon(8% 0,100% 0,92% 100%,0 100%);color:#fff;text-align:center;font-family:"Cinzel",Georgia,serif}
.estimate .big{font-size:36px;line-height:44px;letter-spacing:1px}
.estimate .sm{font-size:20px;letter-spacing:1px}
.years{left:650px;top:392px;width:470px;text-align:center;color:var(--green);font-weight:700;font-size:25px}

/* section titles */
.title{width:1200px;text-align:center;font-family:"Cinzel",Georgia,serif;font-size:36px;color:var(--green);letter-spacing:1px}
.rule{left:480px;width:240px;height:2px;background:linear-gradient(90deg,transparent,var(--green),transparent)}

/* expertise */
.lead{width:1200px;text-align:center;font-size:24px;color:#333}
.skill{width:180px;text-align:center}
.skill .ring{width:100px;height:100px;border-radius:50%;border:2px solid var(--green);margin:0 auto;display:flex;align-items:center;justify-content:center}
.skill .ring span{width:80px;height:80px;border-radius:50%;background:var(--green);display:flex;align-items:center;justify-content:center}
.skill p{margin-top:14px;font-size:22px;color:#222}

/* about */
.about-band{left:0;top:930px;width:1200px;height:410px;background:var(--grey-bg)}
.about-title{left:80px;top:970px;font-family:"Cinzel",Georgia,serif;font-size:34px;color:var(--green)}
.about-title b{color:var(--green);font-weight:700}
.about-rule{left:80px;top:1025px;width:660px;height:2px;background:linear-gradient(90deg,var(--green),transparent)}
.about-text{left:80px;top:1045px;width:670px;font-size:15px;line-height:27px;color:#333}
.btn-green{background:var(--green);color:#fff;font-size:13px;font-weight:700;border-radius:3px;display:flex;align-items:center;justify-content:center}
.hire{left:790px;top:970px;width:330px;height:300px;background:#fff;box-shadow:0 1px 4px rgba(0,0,0,.2)}
.hire-head{height:80px;background:var(--navy);clip-path:polygon(0 0,100% 0,100% 70%,50% 100%,0 70%);color:#fff;font-size:28px;text-align:center;padding-top:12px}
.field{position:absolute;left:20px;width:290px;height:40px;border:1px solid #ccc;border-radius:3px;font-size:13px;color:#333;padding:11px 12px}
.field em{color:#c00;font-style:normal}
.submit{position:absolute;left:20px;top:250px;width:290px;height:40px;background:var(--green);color:#fff;font-family:"Cinzel",Georgia,serif;font-size:20px;font-weight:700;letter-spacing:2px;display:flex;align-items:center;justify-content:center;border-radius:3px}

/* services */
.hexes{left:0;top:1470px}
.build{width:1200px;text-align:center;font-size:27px;font-weight:600;color:#222}
.view-all{left:580px;top:2096px;width:240px;height:52px;background:var(--navy);color:#fff;font-family:"Cinzel",Georgia,serif;font-size:24px;display:flex;align-items:center;justify-content:center}

/* gallery */
.gallery-band{left:0;top:2200px;width:1200px;height:260px;background:var(--grey-bg)}
.gallery-text{width:1200px;text-align:center;font-size:16px;line-height:26px;color:#333}
.tabs{top:2392px;left:420px;display:flex;gap:38px;font-size:18px;color:#444}
.tabs span{display:flex;align-items:center;gap:6px}
.tabs .on{color:var(--green);border-bottom:2px solid var(--green);font-weight:600}
.tabs i{width:14px;height:14px;background:#777;display:inline-block}
.tabs .on i{background:var(--green)}
.shot{top:2455px;width:300px;height:193px}
.overlay{left:12px;top:2466px;width:276px;height:170px;border:1px solid rgba(255,255,255,.6);color:#fff;font-size:20px;padding:60px 0 0 28px}
.overlay .pill{margin-top:10px;width:130px;height:32px;border-radius:16px;background:var(--navy);font-size:14px;display:flex;align-items:center;justify-content:center}
.cta{left:0;top:2648px;width:1200px;height:153px;background:var(--green)}
.cta h3{position:absolute;top:26px;width:1200px;text-align:center;color:#fff;font-weight:400;font-size:29px;letter-spacing:1px}
.cta .pill{position:absolute;left:508px;top:80px;width:184px;height:38px;border-radius:19px;background:var(--navy);color:#fff;font-size:15px;display:flex;align-items:center;justify-content:center}

/* reviews */
.avatar{left:528px;top:2940px;width:144px;height:144px;border-radius:50%;background:var(--navy);padding:8px}
.avatar div{width:100%;height:100%;border-radius:50%;background:linear-gradient(180deg,#d9d9d9,#a8a8a8)}
.reviewer{width:1200px;text-align:center;top:3092px;font-family:"Cinzel",Georgia,serif;color:var(--green);font-size:19px}
.quote{left:140px;top:3132px;width:920px;text-align:center;font-size:14px;line-height:25px;color:#333}
.qm{font-family:Georgia,serif;font-size:90px;color:#d4d4d4;line-height:1}
.dots{top:3222px;left:578px;display:flex;gap:8px}
.dots i{width:10px;height:10px;border-radius:50%;background:#bbb;display:block}
.dots i:first-child{background:var(--navy)}

/* contact band */
.contact{left:0;top:3277px;width:1200px;height:115px;background:var(--navy);color:#fff}
.cblock{position:absolute;top:22px;display:flex;align-items:center;gap:20px}
.cblock .ic{width:72px;height:72px;border-radius:50%;background:#fff;display:flex;align-items:center;justify-content:center}
.cblock .txt{font-size:24px;line-height:30px}
.cblock .txt small{font-size:19px;display:block}

/* footer */
.footer{left:0;top:3392px;width:1200px;height:327px;background:var(--footer);color:#ccc}
.fcol{position:absolute;top:32px}
.fcol h4{font-family:"Cinzel",Georgia,serif;font-weight:400;font-size:20px;color:#fff;letter-spacing:1px;margin-bottom:10px;padding-bottom:8px;border-bottom:1px solid #555;width:170px}
.fcol ul{list-style:none;font-size:14px;line-height:24px}
.fcol li::before{content:"› ";color:#888}
.fcol li.on{color:#fff;font-weight:700}
.fsep{top:32px;width:1px;height:200px;background:#444}
.social{display:flex;gap:10px;margin-top:16px}
.social i{width:32px;height:32px;border-radius:50%;background:#3d5a9a;display:block}
.social i+i{background:#8a8a8a}
.copy{top:3672px;width:1200px;text-align:center;font-size:14px;color:#bbb}
</style>
</head>
<body>

<!-- header -->
<div class="abs topbar"><span class="dot"></span><span class="dot"></span><span class="phone"><i></i>555-010-4477</span></div>
<div class="abs brand">Larkfield Builders LLC<small>LICENSED &amp; INSURED</small></div>
<nav class="abs nav">
  <svg class="home" viewBox="0 0 24 24"><path d="M2 12 12 3l10 9h-3v9h-5v-6h-4v6H5v-9z" fill="#0b4d2c"/></svg>
  <span>About Us</span><span>Services</span><span>Gallery</span><span>Contact Us</span>
</nav>

<!-- hero -->
<div class="abs hero-photo" role="img" aria-label="Photo of a finished wood-cabinet kitchen with granite island and pendant lights"></div>
<svg class="abs hero-accent" viewBox="0 0 90 340" aria-hidden="true"><polygon points="10,0 60,0 90,340 40,340" fill="#3d4f85"/><polygon points="0,0 14,0 44,340 30,340" fill="#fff"/></svg>
<svg class="abs hero-curve" viewBox="0 0 1200 190" preserveAspectRatio="none" aria-hidden="true">
  <path d="M0 190 L0 160 Q500 20 1200 0 L1200 190 Z" fill="#fff"/>
  <path d="M0 160 Q500 20 1200 0 Q520 40 0 175 Z" fill="#3d4f85"/>
</svg>
<div class="abs hero-brand"><div class="name">Larkfield Builders LLC</div><div class="tag">LICENSED &amp; INSURED</div></div>
<div class="abs estimate"><div class="big">FREE ESTIMATES</div><div class="sm">LICENESED &amp; FULLY INSURED</div></div>
<div class="abs years">20 YEARS OF EXPERIENCE</div>

<!-- expertise -->
<h2 class="abs title" style="top:582px">Our Expertise</h2>
<div class="abs rule" style="top:640px"></div>
<p class="abs lead" style="top:678px">We Specialize in Residential Construction. We Are Tile &amp; Marble Specialist</p>

<div class="abs skill" style="left:59px;top:743px"><div class="ring"><span><svg width="44" height="44" viewBox="0 0 44 44"><g fill="none" stroke="#fff" stroke-width="3"><rect x="10" y="10" width="24" height="24" transform="rotate(45 22 22)"/><line x1="5" y1="22" x2="39" y2="22"/><line x1="22" y1="5" x2="22" y2="39"/></g></svg></span></div><p>TILE</p></div>
<div class="abs skill" style="left:260px;top:743px"><div class="ring"><span><svg width="44" height="44" viewBox="0 0 44 44"><rect x="6" y="24" width="32" height="12" fill="#fff"/><rect x="12" y="10" width="16" height="8" fill="#fff"/><rect x="26" y="13" width="10" height="3" fill="#fff"/></svg></span></div><p>CEMENT WORK</p></div>
<div class="abs skill" style="left:460px;top:743px"><div class="ring"><span><svg width="44" height="44" viewBox="0 0 44 44"><g fill="#fff"><circle cx="16" cy="14" r="7"/><circle cx="30" cy="20" r="6"/><circle cx="18" cy="31" r="7"/></g></svg></span></div><p>SIDEWALKS</p></div>
<div class="abs skill" style="left:637px;top:743px"><div class="ring"><span><svg width="44" height="44" viewBox="0 0 44 44"><g fill="none" stroke="#fff" stroke-width="3"><path d="M6 16h32M10 16v20M34 16v20M22 16v20M6 10l16-4 16 4"/></g></svg></span></div><p>DECKS</p></div>
<div class="abs skill" style="left:805px;top:743px"><div class="ring"><span><svg width="44" height="44" viewBox="0 0 44 44"><g fill="none" stroke="#fff" stroke-width="3"><rect x="8" y="8" width="28" height="28"/><path d="M14 30 30 14"/></g></svg></span></div><p>SHEETROCK</p></div>
<div class="abs skill" style="left:976px;top:743px"><div class="ring"><span><svg width="44" height="44" viewBox="0 0 44 44"><g fill="#fff"><rect x="20" y="6" width="16" height="12" transform="rotate(45 28 12)"/><rect x="8" y="24" width="6" height="16" transform="rotate(45 11 32)"/></g></svg></span></div><p>PAINTING</p></div>

<!-- about -->
<div class="abs about-band"></div>
<h2 class="abs about-title">About <b>Larkfield Builders Llc</b></h2>
<div class="abs about-rule"></div>
<p class="abs about-text">Your Home Is The Most Important Asset You Have, So When You're Ready To Build Or Remodel, Get Yourself The Best General Contractor In The Business!<br>We Have Been Building For Over 20 Years, Specializing In Residential Construction. We Are Tile &amp; Marble Specialist. We Build Bathrooms, Kitchens, Additions And Much More. Give Us A Try, We Do Great Work And Are Very Passionate About What We Do. We Are A Family Owned Business That Has Been In The Construction Field For Over 20 Years.</p>
<div class="abs btn-green" style="left:80px;top:1220px;width:90px;height:40px">Read More</div>

<form class="abs hire">
  <div class="hire-head">Hire Us Today</div>
  <div class="field" style="top:100px">Name<em>*</em></div>
  <div class="field" style="top:150px">Email<em>*</em></div>
  <div class="field" style="top:200px">Select Services<em>*</em><span style="float:right;color:#888">⌄</span></div>
  <div class="submit">SUBMIT</div>
</form>

<!-- services -->
<h2 class="abs title" style="top:1370px">Our Services</h2>
<div class="abs rule" style="top:1428px"></div>

<svg class="abs hexes" width="1200" height="500" viewBox="0 0 1200 500" font-family="Open Sans, Arial, sans-serif">
  <defs>
    <linearGradient id="edge" x1="0" y1="0" x2="0" y2="1"><stop offset="0" stop-color="#3d4f85"/><stop offset="1" stop-color="#0b4d2c"/></linearGradient>
  </defs>
  <g stroke="url(#edge)" stroke-width="6">
    <polygon role="img" aria-label="Ceramic flooring work in progress" points="120,5 236,72 236,206 120,273 4,206 4,72" fill="#b7b3ac"/>
    <polygon role="img" aria-label="Marble tile floor with inlay" points="360,5 476,72 476,206 360,273 244,206 244,72" fill="#c9bca5"/>
    <polygon role="img" aria-label="Room with hardwood flooring" points="600,5 716,72 716,206 600,273 484,206 484,72" fill="#8c6a4a"/>
    <polygon role="img" aria-label="Wooden front door" points="840,5 956,72 956,206 840,273 724,206 724,72" fill="#7a3a22"/>
    <polygon role="img" aria-label="House exterior with new windows" points="1080,5 1196,72 1196,206 1080,273 964,206 964,72" fill="#a59c84"/>
    <polygon role="img" aria-label="Tools and materials" points="0,219 116,286 116,420 0,487 -116,420 -116,286" fill="#8f8a82"/>
    <polygon role="img" aria-label="Sheetrock installation" points="240,219 356,286 356,420 240,487 124,420 124,286" fill="#9a7656"/>
    <polygon role="img" aria-label="Kitchen with granite countertops" points="480,219 596,286 596,420 480,487 364,420 364,286" fill="#6b3220"/>
    <polygon role="img" aria-label="Modern bathroom" points="720,219 836,286 836,420 720,487 604,420 604,286" fill="#c2c2c2"/>
    <polygon role="img" aria-label="Painter at work on a wall" points="960,219 1076,286 1076,420 960,487 844,420 844,286" fill="#d9b53a"/>
    <polygon role="img" aria-label="Brick exterior work" points="1200,219 1316,286 1316,420 1200,487 1084,420 1084,286" fill="#8a5a3e"/>
  </g>
  <g fill="#fff" font-size="14" font-weight="700" text-anchor="middle">
    <text x="120" y="222">CERAMIC</text><text x="120" y="238">FLOORING</text>
    <text x="360" y="222">MARBLE</text><text x="360" y="238">FLOORING</text>
    <text x="600" y="222">HARDWOOD</text><text x="600" y="238">FLOORING</text>
    <text x="840" y="222">DOORS</text>
    <text x="1080" y="222">WINDOWS</text>
    <text x="240" y="456">SHEETROCK</text>
    <text x="480" y="456">KITCHENS</text>
    <text x="720" y="456">BATHROOMS</text>
    <text x="960" y="456">PAINTING</text>
  </g>
</svg>

<p class="abs build" style="top:2030px">WE BUILD BATHROOMS, KITCHENS, ADDITIONS &amp; MUCH MORE</p>
<div class="abs view-all">View All Services</div>

<!-- gallery -->
<div class="abs gallery-band"></div>
<h2 class="abs title" style="top:2236px">Our Gallery</h2>
<div class="abs rule" style="top:2292px"></div>
<p class="abs gallery-text" style="top:2320px">Here Are A Few Of Many Projects We Have Completed For Our Customers. We Provide A Professional Service<br>Which Includes Consultation, Free Estimate, Design, Supply Of Materials And Installation.</p>
<div class="abs tabs"><span class="on"><i></i>All</span><span><i></i>Kitchen</span><span><i></i>Kitchen</span><span><i></i>Bathroom</span></div>

<div class="abs shot" style="left:0;background:linear-gradient(135deg,#3a2414,#7a4a28)" role="img" aria-label="Renovated wood-panelled kitchen"></div>
<div class="abs shot" style="left:300px;background:linear-gradient(135deg,#6a4a30,#b8936a)" role="img" aria-label="Framing and stone fireplace under construction"></div>
<div class="abs shot" style="left:600px;background:linear-gradient(180deg,#dcdcdc,#4a4036)" role="img" aria-label="New deck with white railing"></div>
<div class="abs shot" style="left:900px;background:linear-gradient(135deg,#7a3a1e,#1f4d4a)" role="img" aria-label="Kitchen with teal tile backsplash"></div>
<div class="abs overlay">Kitchen Renovation<div class="pill">View Projects</div></div>

<div class="abs cta"><h3>NEED A CONSTRUCTION OR REMOELING ?</h3><div class="pill">View All Projects</div></div>

<!-- reviews -->
<h2 class="abs title" style="top:2854px">Customer Reviews</h2>
<div class="abs rule" style="top:2910px"></div>
<div class="abs avatar"><div role="img" aria-label="Customer portrait"></div></div>
<p class="abs reviewer">- Mr. Daniel Marlow</p>
<span class="abs qm" style="left:80px;top:3112px">“</span>
<p class="abs quote">Lorem ipsum dolor sit amet, consectetuer adipiscing elit, sed diam nonummy nibh euismod tincidunt ut laoreet dolore magna aliquam erat volutpat. Ut wisi enim ad minim veniam, quis nostrud exerci tation ullamcorper suscipit lobortis nisl ut aliquip ex ea commodo consequat. Duis autem vel eum iriure dolor in hendrerit in vulputate velit esse molestie consequat, vel illum.</p>
<span class="abs qm" style="left:1082px;top:3150px">”</span>
<div class="abs dots"><i></i><i></i><i></i></div>

<!-- contact -->
<div class="abs contact">
  <div class="cblock" style="left:80px"><div class="ic"><svg width="32" height="32" viewBox="0 0 24 24"><path d="M6.6 10.8a15 15 0 0 0 6.6 6.6l2.2-2.2c.3-.3.7-.4 1-.2 1.1.4 2.3.6 3.6.6.6 0 1 .4 1 1V20c0 .6-.4 1-1 1A17 17 0 0 1 3 4c0-.6.4-1 1-1h3.5c.6 0 1 .4 1 1 0 1.3.2 2.5.6 3.6.1.3 0 .7-.2 1z" fill="#3d4f85"/></svg></div><div class="txt">Phone:<small>555-010-2550 ,555-010-2549</small></div></div>
  <div class="cblock" style="left:437px"><div class="ic"><svg width="34" height="34" viewBox="0 0 24 24"><path d="M12 2a7 7 0 0 0-7 7c0 5 7 13 7 13s7-8 7-13a7 7 0 0 0-7-7zm0 9.5A2.5 2.5 0 1 1 12 6.5a2.5 2.5 0 0 1 0 5z" fill="#3d4f85"/></svg></div><div class="txt" style="font-size:22px">48 Orchard Ln.<br>Millbrook , New Jersey</div></div>
  <div class="cblock" style="left:770px"><div class="ic"><svg width="30" height="30" viewBox="0 0 24 24"><path d="M3 5h18v14H3z" fill="#3d4f85"/><path d="M3 5l9 8 9-8" fill="none" stroke="#fff" stroke-width="2"/></svg></div><div class="txt">E-mail:<small>hello@larkfieldbuilders.example</small></div></div>
</div>

<!-- footer -->
<footer class="abs footer">
  <div class="fcol" style="left:80px"><h4>Overview</h4><ul><li class="on">Home</li><li>About Us</li><li>Services</li><li>Gallery</li><li>Contact Us</li></ul></div>
  <div class="abs fsep" style="left:250px"></div>
  <div class="fcol" style="left:278px"><h4>Services</h4><ul><li>Ceramic Flooring</li><li>Marble Flooring</li><li>Hardwood Flooring</li><li>Doors</li><li>Windows</li><li>Sheetrock</li></ul></div>
  <div class="fcol" style="left:470px;top:75px"><ul><li>Kitchens</li><li>Bathrooms</li><li>Painting</li><li>Plaster</li><li>Cement</li><li>Decks</li></ul></div>
  <div class="fcol" style="left:620px;top:75px"><ul><li>Pavers</li><li>Additions</li><li>Basements</li></ul></div>
  <div class="abs fsep" style="left:770px"></div>
  <div class="fcol" style="left:798px"><h4 style="width:240px">Our Business Hours</h4><ul><li>Monday to Friday : 10 am to 5 pm</li><li>Saturday : 10 am to 3 pm</li><li>Sunday : Close</li></ul><div class="social"><i></i><i></i></div></div>
  <svg class="abs" style="left:0;top:240px" width="1200" height="40" viewBox="0 0 1200 40" preserveAspectRatio="none" aria-hidden="true"><path d="M0 40 Q600 -10 1200 40 Z" fill="#151515"/></svg>
</footer>
<p class="abs copy">© 2016-2017 Larkfield Builders Llc . All Rights Reserved</p>

</body>
</html>
```